Stylish, Masculine Design - Men's Clothing

Harborline Jacket Mart is a 14,000 square foot warehouse outlet store open to the public since 2005. 50+ brands. Well-known designer brand names and private labels. 30-80% off retail everyday. Lowest prices guaranteed. Average suit price $150. Average shirt price $20. One-stop shop shopping. Men's suits, tuxedos, tuxedo rentals, dress shirts, ties, dress shoes, boy's suits and tuxedos, clergy robes, clergy shirts, cologne, loungewear. Slim fits (Prom Dance), business styles, "church" fashion, security-related uniform. Alterations done by expert tailors on premises for an extra charge.
The final design for both business card and logo should portray stylishness and masculinity.
Updates
We will be changing our name. Details below.New name: Harborline Jacket & Gown name: Harborline Jacket Mart Added Monday, December 26, 2016
Target Market(s)
Gender: 80% Male, 15% Female, 5% Transgender
Location: 80% 10 Mile Radius, 20% >10 Mile Radius
Age: 17-18 (Primarily prom), 18-35 (Primarily Interviews and Weddings), 36-70 (primarily Church and events)
Race: African-American 50%, Latino-American 20%, White 15%, 10% Asian 5% Other
Religions: Christian 50%, 20% Catholic, 10% Mormon, 20% Other/None
Occupation: Local government 40%, Large corporation employee 20%, Small business employee 10%, Small business owner 10%, 20% Unemployed (high school, college)
Education: High School or equivalent 40%, College 30%, Some College 20%, Masters/Doctors 10%
Industry/Entity Type
Retail
Contact Information for Business Card
Name: Darren Kolby
Title: Sales Associate
Address: 518 E. Pimbrook Ave. Gardena, CA 90261
Phone Number: 310.555.0183
Slogan: Warehouse Selection. Outlet Prices, Outstanding Service
www.harborlinejacketmart.example
Logo Text
HJM (Acronym for Harborline Jacket Mart) or Image
Requirements
Must have
- Easy to read
- Visually appealing

```html
<!DOCTYPE html>
<html lang="en">
<head>
<meta charset="utf-8">
<title>Harborline Jacket Mart – Business Card</title>
<link rel="stylesheet" href="https://fonts.googleapis.com/css2?family=Roboto:wght@400;500;700&display=swap">
<style>
  :root {
    --backdrop: #1f1f1f;
    --card: #ffffff;
    --ink: #2b2b2b;
    --muted: #555555;
    --red: #e31e26;
  }
  * { margin: 0; padding: 0; box-sizing: border-box; }
  html, body {
    width: 1200px; height: 1000px; overflow: hidden;
    background: var(--backdrop);
    font-family: "Roboto", Arial, sans-serif;
  }
  .card {
    position: absolute; left: 180px; top: 260px;
    width: 840px; height: 480px;
    background: var(--card);
    border-radius: 30px;
    overflow: hidden;
  }
  .brand {
    position: absolute; left: 250px; top: 78px;
    display: flex; align-items: center; gap: 16px;
  }
  .brand-mark {
    width: 34px; height: 34px; background: var(--red);
  }
  .brand-name {
    font-weight: 700; font-size: 34px; color: var(--ink);
    letter-spacing: 0.5px;
  }
  .divider {
    position: absolute; left: 50px; right: 0; top: 300px;
    height: 3px; background: var(--red);
  }
  .person { position: absolute; left: 50px; top: 218px; }
  .person-name {
    font-weight: 700; font-size: 40px; color: var(--ink);
    line-height: 1; text-transform: uppercase;
  }
  .person-name .surname { color: var(--red); }
  .person-title {
    margin-top: 8px; font-weight: 700; font-size: 21px; color: var(--muted);
  }
  .contacts {
    position: absolute; left: 52px; top: 320px;
    list-style: none;
  }
  .contacts li {
    display: flex; align-items: center; gap: 20px;
    height: 32px; font-size: 21px; color: var(--muted);
  }
  .contacts svg { width: 20px; height: 20px; fill: var(--red); flex: none; }
  .slogan {
    position: absolute; right: 40px; top: 322px;
    text-align: right; font-size: 20px; color: var(--muted); line-height: 28px;
  }
  .slogan .last { margin-top: 4px; display: block; }
  .footer-band {
    position: absolute; left: 0; right: 0; bottom: 0; height: 62px;
    background: var(--red);
    display: flex; align-items: center; justify-content: center;
  }
  .website {
    color: #ffffff; font-size: 27px; letter-spacing: 0.5px; padding-left: 120px;
  }
</style>
</head>
<body>
  <main class="card">
    <div class="brand">
      <span class="brand-mark"></span>
      <span class="brand-name">Harborline Jacket &amp; Gown</span>
    </div>

    <div class="person">
      <h1 class="person-name">Darren <span class="surname">Kolby</span></h1>
      <p class="person-title">Sales Associate</p>
    </div>

    <div class="divider"></div>

    <ul class="contacts">
      <li>
        <svg viewBox="0 0 24 24" aria-hidden="true"><path d="M6.6 10.8c1.4 2.8 3.8 5.1 6.6 6.6l2.2-2.2c.3-.3.7-.4 1-.2 1.1.4 2.3.6 3.6.6.6 0 1 .4 1 1V20c0 .6-.4 1-1 1C10.6 21 3 13.4 3 4c0-.6.4-1 1-1h3.5c.6 0 1 .4 1 1 0 1.3.2 2.5.6 3.6.1.3 0 .7-.2 1L6.6 10.8z"/></svg>
        <span>310 555 0183</span>
      </li>
      <li>
        <svg viewBox="0 0 24 24" aria-hidden="true"><path d="M2 5h20v14H2z M4 7v.5l8 5.5 8-5.5V7z" fill-rule="evenodd"/></svg>
        <span>dkolby@harborlinejacketmart.example</span>
      </li>
      <li>
        <svg viewBox="0 0 24 24" aria-hidden="true"><path d="M12 2a7 7 0 0 0-7 7c0 5.2 7 13 7 13s7-7.8 7-13a7 7 0 0 0-7-7zm0 9.5A2.5 2.5 0 1 1 12 6.5a2.5 2.5 0 0 1 0 5z"/></svg>
        <span>518 E. Pimbrook Ave. Gardena, CA 90261</span>
      </li>
    </ul>

    <p class="slogan">
      Warehouse Selection<br>
      Outlet Prices<br>
      <span class="last">Outstanding Service</span>
    </p>

    <footer class="footer-band">
      <span class="website">www.harborlinejacketmart.example</span>
    </footer>
  </main>
</body>
</html>
```